Company brochure for our unique consulting business

We are a small consulting business offering a unique set of services to our clients.. In simple terms we are a business improvement consultancy helping our clients get the best out of their businesses. We work with clients across multiple sectors and deliver a variety of services. We want to put together a brochure to cover these main themes:1. Who we are2. What we do3. The type of people we employ4. The sectors we work inWhile the brochure needs to have a certain corporate feel to it, we don't want it to be "boring" or "stiff". We would like it to have a slightly "friendly" or "informal" feel to it, to reflect the type of organisation we are.We have a company website http://tollandvergeadvisory.com , however we do not want to directly replicate the content or feel as we recognise it needs updating.We would like the brochure to be A4 portrait format. We anticipate requiring 12 sides (including covers) but we are happy to be guided on this based on the content we have provided.The attached ppt file gives the detail of the content to be included and also shows the proposed pagination. For the front cover we would like to try 2 versions, one with the TVA logo and one with the Tolland Verge Advisory logo (a file of both is attached)One of the most important pages will be the "Our Services" page. We would like this to cover the centre fold. In the ppt file we have shown an example layout, but this is where we need most help - we are clearly not graphic designers! This page will be the most used page in sales meetings etc.Also attached is the following:1. file for our TollandVerge Advisory company logo.2. File for our TVA company logo3. Files for Derek's signatures (for under photos) - Owen's to follow4. Photo of Derek & Owen (person in purple shirt to be cropped out)Thank you and really excited to see what everyone comes back with.Derek & Owen

Target Market(s)

Very broad - Manufacturing, Healthcare, Hospitality

Industry/Entity Type

Management Consulting

Font styles to use
Other font styles liked:
• We use Swiss721, but happy to be guided by designer

Colors
3276b5
85abd2
0355a3
333333
5c5c5c
9d9d9d
d9d9d9

Requirements
Must have
• Corporate feel
Nice to have
• Slightly friendly feel
• Our standard "blue" is (CORRECTION) - R55 G96 B146 #376092 and our standard grey is R197 G178, B179 - #B3B2B2, which we would like to keep, but other colours we are happy to be guided on. Brand guidelines attached.

```html
<!DOCTYPE html>
<html lang="en">
<head>
<meta charset="utf-8">
<title>Tolland Verge Advisory – Brochure Spreads</title>
<link rel="stylesheet" href="https://fonts.googleapis.com/css2?family=Roboto:wght@400;500;700&display=swap">
<style>
  :root {
    --canvas: #b4b5b7;
    --brand-blue: #2f619b;
    --blue-deep: #2c5a91;
    --blue-bright: #3276b5;
    --blue-column: #2e5f99;
    --blue-rule: #85abd2;
    --ink: #333333;
    --white: #ffffff;
  }
  * { box-sizing: border-box; margin: 0; padding: 0; }
  html, body { width: 921px; height: 1200px; overflow: hidden; }
  body {
    background: var(--canvas);
    font-family: "Roboto", Arial, sans-serif;
    position: relative;
  }
  .edge-strip { position: absolute; left: 69px; width: 787px; height: 2px; }
  .edge-strip--top { top: 0; background: linear-gradient(90deg, #e8e8e8 50%, #f4f4f4 50%); }
  .edge-strip--bottom { bottom: 0; background: linear-gradient(90deg, var(--brand-blue) 50%, #f4f4f4 50%); }

  .spread { position: absolute; left: 69px; width: 787px; height: 556px; overflow: hidden; }
  .spread--people { top: 36px; background: var(--white); }
  .spread--services { top: 609px; }

  .photo { position: absolute; }
  .photo--office {
    left: 0; top: 0; width: 478px; height: 556px;
    background:
      linear-gradient(180deg, rgba(255,255,255,0) 45%, rgba(120,120,120,.25) 62%, rgba(255,255,255,.2) 100%),
      linear-gradient(90deg, #e4e4e4 0%, #cfcfcf 40%, #9a9a9a 65%, #b8b8b8 80%, #8a8a8a 100%);
  }
  .photo--tablet {
    left: 0; top: 0; width: 787px; height: 556px;
    background:
      linear-gradient(90deg, rgba(0,0,0,0) 50%, rgba(0,0,0,.35) 50%),
      radial-gradient(ellipse at 30% 55%, #8e8e8e 0%, #5f5f5f 45%, #3a3a3a 100%),
      #4a4a4a;
  }
  .page-seam { position: absolute; top: 0; left: 393px; width: 1px; height: 100%; background: rgba(0,0,0,.12); }

  .blue-panel { position: absolute; left: 0; top: 0; }

  .section-title {
    position: absolute; color: var(--white); font-weight: 500; display: flex; align-items: center; gap: 5px;
  }
  .section-title .slashes { font-weight: 700; font-style: italic; letter-spacing: -2px; }
  .people-title { left: 41px; top: 137px; font-size: 17px; }
  .people-copy {
    position: absolute; left: 41px; top: 173px; width: 145px;
    color: var(--white); font-size: 7.4px; line-height: 9.4px; text-align: justify;
  }
  .people-copy p + p { margin-top: 24px; }

  .quotes { position: absolute; left: 501px; top: 0; width: 228px; }
  .quotes-title {
    position: absolute; left: 0; top: 20px; color: var(--brand-blue); font-size: 16px; font-weight: 500;
    display: flex; gap: 5px;
  }
  .quotes-title .slashes { font-weight: 700; font-style: italic; letter-spacing: -2px; }
  .quote { position: absolute; left: 0; width: 228px; }
  .quote-text { font-size: 7.2px; line-height: 9.4px; color: var(--ink); text-align: justify; }
  .quote-text b { font-weight: 700; }
  .quote-source { text-align: center; color: var(--brand-blue); font-size: 9px; line-height: 11px; margin-top: 19px; }
  .quote-source .role { font-weight: 700; }

  .services-title { left: 41px; top: 223px; font-size: 16.5px; }
  .services-copy {
    position: absolute; left: 41px; top: 255px; width: 168px;
    color: var(--white); font-size: 7.4px; line-height: 9.4px; text-align: justify;
  }

  .service-column { position: absolute; top: 96px; width: 100px; color: var(--white); text-align: center; }
  .service-column svg.column-shape { position: absolute; left: 0; top: 0; }
  .column-head { position: relative; height: 89px; padding-top: 10px; }
  .column-icon { display: block; margin: 0 auto 4px; }
  .column-name { font-size: 9px; line-height: 11px; font-weight: 500; }
  .column-tag { font-size: 5.6px; line-height: 7px; font-weight: 700; margin-top: 5px; padding: 0 8px; }
  .column-list { position: relative; list-style: none; padding: 9px 8px 0; font-size: 5.8px; line-height: 7px; }
  .column-list li { margin-bottom: 9.5px; }
</style>
</head>
<body>
  <div class="edge-strip edge-strip--top"></div>

  <section class="spread spread--people">
    <div class="photo photo--office" role="img" aria-label="Silhouettes of business people talking by a bright office window, reflected on the floor"></div>
    <svg class="blue-panel" width="260" height="556" aria-hidden="true">
      <polygon points="0,0 195,0 256,276 191,556 0,556" fill="var(--brand-blue)" opacity="0.93"/>
    </svg>
    <div class="page-seam"></div>

    <h2 class="section-title people-title"><span class="slashes">////</span> Our People</h2>
    <div class="people-copy">
      <p>All of our team at TVA started their careers in operational roles. This means we understand what it's like to be in your shoes. Blending this understanding with our years of experience and skills we are able to work in partnership with you and your teams to deliver great results, together. Simply put, our team has some of the best people in the industry.</p>
      <p>We also recognise no single person knows everything, so within the team we have experts in their own fields. They are able to bring their specialised skills and experience, at the right time and in the best way possible.</p>
      <p>Our team also understand the importance of engagement. Everyone in your team will get to know us on first name terms, because we take the time to listen to everyone, from shop floor to senior management</p>
    </div>

    <div class="quotes">
      <h2 class="quotes-title"><span class="slashes">////</span> Quotes</h2>
      <div class="quote" style="top:76px">
        <p class="quote-text"><b>TVA</b> have achieved excellent engagement throughout the entire organisation with significant measurable successes.</p>
        <p class="quote-source"><span class="role">Director of Operations</span><br>Harlow Sorting</p>
      </div>
      <div class="quote" style="top:153px">
        <p class="quote-text">With the team from <b>TVA</b> we have been able to embed an improvement approach across the entire organisation.</p>
        <p class="quote-source"><span class="role">Chief Operations Officer</span><br>Wyvern General Hospital</p>
      </div>
      <div class="quote" style="top:234px">
        <p class="quote-text">You have definitely made our lives easier knowing that you are taking care of our British colleagues. If we have future needs, we will definitely be straight back to you.</p>
        <p class="quote-source"><span class="role">Chief Operations Officer</span><br>Ashcombe Games</p>
      </div>
      <div class="quote" style="top:330px">
        <p class="quote-text">The team from <b>TVA</b> have been invaluable with helping implement our lean programme. They've helped break down what seemed very complicated at the start, into logical and simple steps.</p>
        <p class="quote-source"><span class="role">Managing Director</span><br>Penmark Supplies</p>
      </div>
      <div class="quote" style="top:432px">
        <p class="quote-text"><b>TVA</b> have been able offer us support across a range of topics based on their in-depth knowledge of lean and Kessai systems</p>
        <p class="quote-source"><span class="role">Continuous Improvement Manager</span><br>Korvell Motors</p>
      </div>
    </div>
  </section>

  <section class="spread spread--services">
    <div class="photo photo--tablet" role="img" aria-label="Hand holding a tablet with a network technology diagram, beside a businessman adjusting his tie"></div>
    <svg class="blue-panel" width="260" height="556" aria-hidden="true">
      <polygon points="0,131 219,131 251,267 219,420 0,420" fill="var(--brand-blue)" opacity="0.9"/>
    </svg>

    <h2 class="section-title services-title"><span class="slashes">////</span> OUR SERVICES</h2>
    <p class="services-copy">We recognise every organisation we work with is different; the products or services provided, the culture and the readiness for change but most importantly the 'wants and needs' are always unique. The skills, knowledge and experience across our team means we are able to offer an extensive range of services which are tailored to meet your specific needs.</p>

    <div class="service-column" style="left:433px">
      <svg class="column-shape" width="100" height="372" aria-hidden="true">
        <rect x="0" y="0" width="100" height="89" fill="var(--blue-bright)"/>
        <rect x="0" y="89" width="100" height="1" fill="var(--blue-rule)"/>
        <polygon points="0,90 100,90 100,355 50,372 0,355" fill="var(--blue-column)"/>
      </svg>
      <div class="column-head">
        <svg class="column-icon" width="16" height="16" viewBox="0 0 16 16" aria-hidden="true">
          <path d="M2 2 L14 14 M14 2 L2 14" stroke="#fff" stroke-width="2.2" stroke-linecap="round"/>
        </svg>
        <div class="column-name">Business<br>Improvement</div>
        <div class="column-tag">Helping your organisation perform at it's best</div>
      </div>
      <ul class="column-list">
        <li>leadership coaching<br>&amp; mentoring</li>
        <li>Process design</li>
        <li>Facility Design</li>
        <li>New Product Introduction</li>
        <li>Logistics and planning</li>
        <li>Equipment design</li>
        <li>Quality systems</li>
        <li>Programme Management<br>&amp; PMO</li>
        <li>Personal Development</li>
        <li>Senior leadership<br>development</li>
        <li>Strategy Development</li>
        <li>Organisational design</li>
        <li>Supply chain development</li>
        <li>Business Assessment</li>
      </ul>
    </div>

    <div class="service-column" style="left:541px">
      <svg class="column-shape" width="100" height="376" aria-hidden="true">
        <rect x="0" y="0" width="100" height="89" fill="var(--blue-bright)"/>
        <rect x="0" y="89" width="100" height="1" fill="var(--blue-rule)"/>
        <polygon points="0,90 100,90 100,363 50,376 0,363" fill="var(--blue-column)"/>
      </svg>
      <div class="column-head">
        <svg class="column-icon" width="16" height="16" viewBox="0 0 16 16" aria-hidden="true">
          <circle cx="8" cy="8" r="6.5" fill="none" stroke="#fff" stroke-width="1.6" stroke-dasharray="8 2"/>
          <circle cx="8" cy="8" r="3" fill="#fff"/>
        </svg>
        <div class="column-name">Programme<br>Management</div>
        <div class="column-tag">Managing programmes through to successful delivery</div>
      </div>
      <ul class="column-list">
        <li>Separation &amp; Mergers</li>
        <li>New Product Introduction</li>
        <li>I.T. System Introduction</li>
        <li>Customer Accreditation</li>
        <li>Facility Relocation</li>
        <li>New Equipment</li>
        <li>Major Events</li>
        <li>ISO</li>
        <li>Cost Improvement<br>Programmes</li>
      </ul>
    </div>

    <div class="service-column" style="left:649px">
      <svg class="column-shape" width="100" height="376" aria-hidden="true">
        <rect x="0" y="0" width="100" height="89" fill="var(--blue-bright)"/>
        <rect x="0" y="89" width="100" height="1" fill="var(--blue-rule)"/>
        <polygon points="0,90 100,90 100,363 50,376 0,363" fill="var(--blue-column)"/>
      </svg>
      <div class="column-head">
        <svg class="column-icon" width="16" height="16" viewBox="0 0 16 16" aria-hidden="true">
          <circle cx="8" cy="8" r="3" fill="#fff"/>
          <path d="M8 1 V4 M8 12 V15 M1 8 H4 M12 8 H15 M3 3 L5 5 M11 11 L13 13 M13 3 L11 5 M5 11 L3 13" stroke="#fff" stroke-width="1.5"/>
        </svg>
        <div class="column-name">Organisational<br>Readiness</div>
        <div class="column-tag">Getting your business ready for it's future</div>
      </div>
      <ul class="column-list">
        <li>Optimisation</li>
        <li>Growth</li>
        <li>Merger</li>
        <li>Separation</li>
        <li>Acquisition</li>
        <li>Sale</li>
      </ul>
    </div>
  </section>

  <div class="edge-strip edge-strip--bottom"></div>
</body>
</html>
```